Building company business card

Design and print business cards for BRENTHOLM PTY LTD.
A residantial homes building company.
Mark Lantern already designed the company Logo.

```html
<!DOCTYPE html>
<html lang="en">
<head>
<meta charset="utf-8">
<title>Brentholm Pty Ltd – Business Card</title>
<link rel="stylesheet" href="https://fonts.googleapis.com/css2?family=Lato:wght@400;700;900&display=swap">
<style>
  :root {
    --backdrop: #1d1d1f;
    --paper: #ffffff;
    --navy: #0f2170;
    --gold: #b7862c;
    --gold-light: #d6a650;
    --ink: #3a3a3a;
  }
  * { margin: 0; padding: 0; box-sizing: border-box; }
  html, body {
    width: 1200px; height: 1200px; overflow: hidden;
    background: var(--backdrop);
    font-family: "Lato", Arial, sans-serif;
  }
  .canvas { position: relative; width: 1200px; height: 1200px; }

  .card {
    position: absolute; left: 250px; width: 700px; height: 400px;
  }
  .card-front { top: 170px; background: var(--paper); }
  .card-back { top: 630px; background: var(--navy); }

  .person {
    position: absolute; right: 378px; top: 164px; text-align: right;
  }
  .person-name {
    color: var(--navy); font-weight: 700; font-size: 23.5px; letter-spacing: -0.2px; line-height: 1;
  }
  .person-role {
    color: var(--gold); font-size: 19px; margin-top: 7px; line-height: 1;
  }
  .person-licence {
    color: var(--ink); font-size: 16px; margin-top: 10px; letter-spacing: 0.4px; line-height: 1;
  }

  .divider {
    position: absolute; left: 351px; top: 102px; width: 2px; height: 196px; background: var(--navy);
  }

  .company { position: absolute; left: 379px; top: 103px; }
  .company-name {
    color: var(--navy); font-size: 17px; letter-spacing: 0.6px; line-height: 24px;
  }
  .company-line {
    color: var(--ink); font-size: 16px; letter-spacing: 0.4px; line-height: 24px;
  }
  .contact-list { list-style: none; margin-top: 7px; }
  .contact-item {
    display: flex; align-items: center; gap: 12px;
    color: var(--ink); font-size: 16px; letter-spacing: 0.4px; line-height: 24px;
  }
  .contact-icon { width: 12px; height: 12px; flex: none; }

  .accent-band { position: absolute; left: 0; bottom: 0; width: 700px; height: 19px; }

  .wordmark {
    position: absolute; left: 0; right: 0; top: 170px; text-align: center;
    color: var(--paper); font-weight: 900; font-size: 50px; letter-spacing: 1px; line-height: 60px;
  }
</style>
</head>
<body>
<main class="canvas">

  <section class="card card-front" aria-label="Business card front">
    <div class="person">
      <p class="person-name">THEODORE (Theo) MARKOS</p>
      <p class="person-role">Director</p>
      <p class="person-licence">CDB-U 48215</p>
    </div>

    <div class="divider"></div>

    <div class="company">
      <p class="company-name">BRENTHOLM PTY LTD</p>
      <p class="company-line">PO Box 482</p>
      <p class="company-line">Kew East, Vic 3102</p>
      <p class="company-line">ABN- 52 418 906 273</p>

      <ul class="contact-list">
        <li class="contact-item">
          <svg class="contact-icon" viewBox="0 0 12 12" aria-hidden="true">
            <path d="M2.5 1 L4.3 3.2 L3.3 4.4 Q4.5 6.9 7.4 8.5 L8.6 7.5 L11 9.3 L9.8 11 Q5.5 10.6 2.2 7 Q0.6 4.4 1 2 Z" fill="var(--gold)"/>
            <path d="M7 1.2 Q10.4 1.8 10.8 5" stroke="var(--gold)" stroke-width="1.1" fill="none"/>
            <path d="M6.8 3.2 Q8.6 3.6 8.9 5.2" stroke="var(--gold)" stroke-width="1.1" fill="none"/>
          </svg>
          <span>0412 555 308</span>
        </li>
        <li class="contact-item">
          <svg class="contact-icon" viewBox="0 0 12 12" aria-hidden="true">
            <rect x="2.5" y="0.6" width="7" height="10.8" rx="1.2" fill="none" stroke="var(--gold)" stroke-width="1.3"/>
            <circle cx="6" cy="9.4" r="0.8" fill="var(--gold)"/>
          </svg>
          <span>0412 555 308 &amp; 0438 555 126</span>
        </li>
        <li class="contact-item">
          <svg class="contact-icon" viewBox="0 0 12 12" aria-hidden="true">
            <rect x="0.6" y="2.4" width="10.8" height="7.4" fill="var(--gold)"/>
            <path d="M0.8 2.8 L6 6.8 L11.2 2.8 M0.8 9.4 L4.6 5.8 M11.2 9.4 L7.4 5.8" stroke="#fff" stroke-width="0.8" fill="none"/>
          </svg>
          <span>tm@brentholm-pl.com</span>
        </li>
        <li class="contact-item">
          <svg class="contact-icon" viewBox="0 0 12 12" aria-hidden="true">
            <circle cx="6" cy="6" r="5.2" fill="none" stroke="var(--gold)" stroke-width="1.3"/>
            <path d="M3.2 3 Q5 4 4.4 5.6 Q5.6 6.6 5 8.8 M7.6 2.2 Q7 4 8.8 4.6 Q9.6 6.2 8.6 8" stroke="var(--gold)" stroke-width="1.2" fill="none"/>
          </svg>
          <span>brentholm-pl.com</span>
        </li>
      </ul>
    </div>

    <svg class="accent-band" viewBox="0 0 700 19" aria-hidden="true">
      <defs>
        <linearGradient id="goldBand" x1="0" y1="0" x2="1" y2="0">
          <stop offset="0" stop-color="var(--gold)"/>
          <stop offset="1" stop-color="var(--gold-light)"/>
        </linearGradient>
      </defs>
      <polygon points="0,0 447,0 430,19 0,19" fill="var(--navy)"/>
      <polygon points="451,0 700,0 700,19 437,19" fill="url(#goldBand)"/>
    </svg>
  </section>

  <section class="card card-back" aria-label="Business card back">
    <p class="wordmark">BRENTHOLM</p>
  </section>

</main>
</body>
</html>
```